Logo & Web Design for Technical Research Products

Logo and Web Design for a little business selling some niche research, technical products. Current site is at: http://ferrowick.com/ferrowick-battery-test-cell. The audience are university researchers, technical labs and similar.

We would like a more professional looking logo and design than what is currently there.

This new design should include/consider:
- A front page with the ability to show-case 2-3 select products
- An About Us page
- A Contact Us page
- An FAQ page
- A hierarchical menu structure (preferably to the left) allowing for at least two levels. (We plan to add more products and categories in the future)
- Include both a Desktop and Phone version (responsive design)
- We plan to have all products follow a similar template so please have that in mind when desiging (Some part of the product template may be omitted for some products if not applicable)
- Multiple images per product should be supported(carousel perhaps?)

When creating the CSS and HTML please use Bootstap 4.
(https://getplinthkit.com/docs/4.0/getting-started/introduction/)

```html
<!DOCTYPE html>
<html lang="en">
<head>
<meta charset="utf-8">
<title>Ferrowick – Technical Research Products</title>
<link href="https://fonts.googleapis.com/css2?family=Poppins:wght@300;400;500;600;700&display=swap" rel="stylesheet">
<style>
:root{
  --teal:#14b3cf;
  --teal-dark:#0e93ab;
  --teal-soft:#bfeaf2;
  --ink:#1f2b33;
  --text:#5d6870;
  --grey-bg:#f2f3f4;
  --line:#dfe3e6;
  --footer:#2d3c45;
  --footer-deep:#25323a;
  --white:#ffffff;
}
*{box-sizing:border-box;margin:0;padding:0}
html,body{width:1200px;height:2764px;overflow:hidden}
body{position:relative;background:var(--white);font-family:"Poppins",sans-serif;color:var(--text)}
.abs{position:absolute}
.brand{font-weight:700;color:var(--ink);letter-spacing:.5px}
.btn{display:inline-block;background:var(--teal);color:var(--white);font-size:11px;font-weight:600;text-transform:uppercase;padding:9px 22px;border-radius:20px}

/* header */
.site-header .brand{left:90px;top:26px;font-size:28px}
.main-nav{left:330px;top:34px;display:flex;gap:34px;font-size:14px;font-weight:500;color:var(--ink)}
.main-nav .active{color:var(--teal)}

/* hero */
.hero-art{left:540px;top:0}
.hero-copy{left:90px;top:290px}
.hero-copy .eyebrow{font-size:36px;font-weight:700;color:var(--ink);line-height:1}
.hero-copy .brand{font-size:68px;line-height:1.15}
.hero-copy p{font-size:15px;width:260px;margin:6px 0 20px;line-height:1.4}
.dots{left:0;top:560px}

/* about */
.about-square{left:130px;top:940px;width:90px;height:220px;background:var(--teal)}
.about-photo{left:160px;top:700px;width:420px;height:360px;background:linear-gradient(135deg,#c9b9a6,#6f6a60 55%,#3e4a4d)}
.about-copy{left:630px;top:800px;width:440px}
.about-copy h2,.section-title{font-size:42px;font-weight:600;color:var(--ink)}
.about-copy h2 span,.section-title span{font-weight:300}
.about-copy p{font-size:13px;line-height:1.75;margin:12px 0 26px}

/* products */
.products{left:0;top:1270px;width:1200px;height:390px;background:var(--grey-bg)}
.products .section-title{position:absolute;left:0;right:0;top:60px;text-align:center}
.product-grid{position:absolute;left:85px;top:130px;display:flex;gap:20px}
.product-card{width:243px;height:210px;background:var(--white);text-align:center;padding-top:14px}
.product-card .shot{width:150px;height:110px;margin:0 auto 10px;border-radius:4px}
.product-card h3{font-size:13px;font-weight:600;color:var(--ink);line-height:1.3}
.product-card .price{font-size:15px;color:var(--ink);margin-top:4px}

/* faq */
.faq{left:85px;top:1865px;width:510px}
.faq .section-title{margin-bottom:26px}
.faq-item{display:flex;justify-content:space-between;align-items:center;border:1px solid var(--line);height:46px;padding:0 18px;margin-bottom:16px;font-size:13px;color:var(--ink)}
.review{left:640px;top:1865px;width:480px}
.review .section-title{margin-bottom:26px}
.review-body{display:flex;gap:22px}
.avatar{width:110px;height:110px;border-radius:50%;background:linear-gradient(135deg,#d7cfc4,#8a7f73);flex:none}
.review-body p{font-size:13px;line-height:1.7}
.review-body .name{color:var(--teal);font-weight:600;font-size:14px;margin-top:6px}
.review-body .role{font-size:11px}
.review .pager{display:flex;gap:6px;margin:10px 0 0 132px}
.review .pager i{width:8px;height:8px;border-radius:50%;background:var(--teal-soft)}
.review .pager i:first-child{background:var(--teal)}

/* footer */
.site-footer{left:0;top:2380px;width:1200px;height:384px;background:var(--footer);color:#c6d0d5}
.site-footer .brand{position:absolute;left:90px;top:144px;font-size:36px;color:var(--white)}
.site-footer h4{font-size:14px;font-weight:600;color:var(--white);margin-bottom:14px}
.quick-links{position:absolute;left:390px;top:48px;font-size:13px;line-height:2.05}
.newsletter{position:absolute;left:585px;top:48px;width:270px;font-size:12px;line-height:1.6}
.newsletter .field{margin-top:14px;height:34px;border:1px solid #4b5b64;border-radius:3px;display:flex;align-items:center;justify-content:space-between;padding:0 10px;color:#8d9aa1}
.contact-info{position:absolute;left:905px;top:48px;font-size:12px;line-height:1.5}
.contact-info .row{display:flex;gap:10px;margin-bottom:16px}
.contact-info b{display:block;color:var(--white);font-weight:500}
.footer-bar{position:absolute;left:0;bottom:0;width:1200px;height:54px;background:var(--footer-deep);display:flex;align-items:center;justify-content:space-between;padding:0 90px;font-size:12px}
.social{display:flex;gap:8px}
.social i{width:22px;height:22px;border-radius:50%;background:#4a5a63}
.to-top{right:14px;top:2716px;width:34px;height:34px;border-radius:50%;background:var(--teal)}
</style>
</head>
<body>

<header class="site-header">
  <div class="abs brand">Ferrowick</div>
  <nav class="abs main-nav">
    <span class="active">Home</span><span>About Us</span><span>Products ▾</span><span>FAQs</span><span>Contact Us</span>
  </nav>
</header>

<svg class="abs hero-art" width="660" height="600" viewBox="0 0 660 600">
  <path d="M70 0 H660 V240 L360 560 Q320 600 280 560 L60 330 Q30 300 40 260 Z" fill="var(--teal)"/>
  <path d="M110 0 H660 V210 L350 540 Q320 570 290 540 L85 320 Q60 295 68 260 Z" fill="url(#heroPhoto)" role="img" aria-label="Photo of a smiling researcher working at a lab bench"/>
  <defs>
    <linearGradient id="heroPhoto" x1="0" y1="0" x2="1" y2="1">
      <stop offset="0" stop-color="#e9eef0"/><stop offset=".5" stop-color="#9fb4bb"/><stop offset="1" stop-color="#3f5660"/>
    </linearGradient>
  </defs>
</svg>

<section class="abs hero-copy">
  <div class="eyebrow">Welcome to</div>
  <div class="brand">Ferrowick</div>
  <p>Business selling some niche research, technical products</p>
  <span class="btn">View Product</span>
</section>

<svg class="abs dots" width="600" height="560" viewBox="0 0 600 560">
  <g fill="var(--teal)">
    <circle cx="20" cy="510" r="9" opacity=".5"/><circle cx="55" cy="520" r="8" opacity=".6"/>
    <circle cx="90" cy="505" r="8" opacity=".7"/><circle cx="120" cy="480" r="7" opacity=".5"/>
    <circle cx="200" cy="300" r="10" opacity=".7"/><circle cx="235" cy="260" r="9" opacity=".6"/>
    <circle cx="275" cy="225" r="8" opacity=".5"/><circle cx="320" cy="205" r="9" opacity=".8"/>
    <circle cx="365" cy="200" r="10" opacity=".6"/><circle cx="410" cy="215" r="7" opacity=".4"/>
  </g>
</svg>

<div class="abs about-square"></div>
<div class="abs about-photo" role="img" aria-label="Photo of a young technician assembling a circuit board"></div>
<section class="abs about-copy">
  <h2>About <span>Us</span></h2>
  <p>Lorem Ipsum is simply dummy text of the printing and typesetting industry. Lorem Ipsum has been the industry's standard dummy text ever since the 1500s, when an unknown printer took a galley of type and scrambled it to make a type specimen book. It has survived not only five centuries, but also the leap into electronic typesetting, remaining essentially unchanged. It was popularised in the 1960s with the release of Letraset sheets containing Lorem Ipsum passages, and more recently.</p>
  <span class="btn">Read More</span>
</section>

<section class="abs products">
  <h2 class="section-title">Our <span>Products</span></h2>
  <div class="product-grid">
    <div class="product-card"><div class="shot" role="img" aria-label="Photo of an 8 channel battery tester" style="background:linear-gradient(#d8dcd6,#8f9a8c)"></div><h3>8 channel<br>battery tester</h3><div class="price">€ 2,700</div></div>
    <div class="product-card"><div class="shot" role="img" aria-label="Photo of a flow battery test cell" style="background:linear-gradient(#9fc2e4,#2f5f9a)"></div><h3>Ferrowick Flow<br>Battery Test Cell</h3><div class="price">€ 1,500</div></div>
    <div class="product-card"><div class="shot" role="img" aria-label="Photo of a photoelectrochemical laboratory test cell" style="background:linear-gradient(#b9b9b9,#4a4a4a)"></div><h3>Photoelectrochemical<br>laboratory test cell</h3><div class="price">€ 2,500</div></div>
    <div class="product-card"><div class="shot" role="img" aria-label="Photo of a 2 channel peristaltic pump" style="background:linear-gradient(#cfcfcf,#333a3e)"></div><h3>2 channel<br>peristaltic pump</h3><div class="price">€ 3,000</div></div>
  </div>
</section>

<section class="abs faq">
  <h2 class="section-title">Our <span>FAQs</span></h2>
  <div class="faq-item">Lorem Ipsum is simply dummy text of the printing?<span>›</span></div>
  <div class="faq-item">Typesetting industry. Lorem Ipsum has been the industry's?<span>›</span></div>
  <div class="faq-item">Standard dummy text ever since the 1500s?<span>›</span></div>
  <div class="faq-item">when an unknown printer took a galley of type and scrambled?<span>›</span></div>
</section>

<section class="abs review">
  <h2 class="section-title">Review</h2>
  <div class="review-body">
    <div class="avatar" role="img" aria-label="Portrait photo of the reviewer"></div>
    <div>
      <p>Lorem Ipsum is simply dummy text of the printing and typesetting industry. Lorem Ipsum has been the industry's standard dummy text ever since the 1500s, when an unknown printer.</p>
      <div class="name">Alan Brooks</div>
      <div class="role">Lab Director</div>
    </div>
  </div>
  <div class="pager"><i></i><i></i><i></i></div>
</section>

<footer class="abs site-footer">
  <div class="brand">Ferrowick</div>
  <div class="quick-links"><h4>Quick Links</h4>Home<br>About Us<br>Products<br>FAQs<br>Contact Us</div>
  <div class="newsletter"><h4>Newsletter</h4>Subscribe to our email address to get the latest news.<div class="field">Enter Your Email<span style="color:var(--teal)">➤</span></div></div>
  <div class="contact-info">
    <h4>Contact Info</h4>
    <div class="row"><span>✉</span><div><b>Email</b>info@ferrowick.com</div></div>
    <div class="row"><span>✆</span><div><b>Phone</b>123-456-7890</div></div>
    <div class="row"><span>⌖</span><div><b>Location</b>Your address line goes here</div></div>
  </div>
  <div class="footer-bar"><span>© Copyright 2019 &nbsp;|&nbsp; All Rights Reserved</span><div class="social"><i></i><i></i><i></i><i></i></div></div>
</footer>
<div class="abs to-top"></div>

</body>
</html>
```